Corvantic Needs a Poster to Advertise a New Membership Offer

We need a Poster design for Corvantic Fitness Guild.
A first of it's kind membership, The Corvantic Fitness Guild combines the skills of our industry-leading Physiotherapists, Strength Coaches and Massage Therapists into one membership with a tailored plan to guide you through the fundamentals of Movement, Mobility and Recovery.
The concept is loosely based on the professional sports model, where every member of our team works together to produce lasting results for you. The final design should illustrate the bespoke nature of our program in a fun, supportive and professional space.
"Whether your aim is to be the best in the world, or the best in your world – it’s all the same to us."
Brand Guidelines
The poster should be on a black background and use our brand colour, lime green (hexcode #cefa08) as a highlight. Please don't overuse the highlight colour though. Generally, we opt for less bright colours and more of a 'street' look
Target Market(s)
The poster should attract predominantly female members, but should not exclude males. The target age range is 30-40 years female.
Industry/Entity Type
Health And Wellness
Requirements
Must have
- Must Include
• CFG logo
• Tag line " Shaping Steady, Nimble, Unbreakable People"
• Call to action "Join us"
• Sized to 600(W)x900(H)mm
• Text: "A first of it's kind membership, The Corvantic Fitness Guild combines the skills of our industry-leading Physiotherapists, Strength Coaches and Massage Therapists into one membership with a tailored plan to guide you through the fundamentals of Movement, Mobility and Recovery."
Nice to have
- Ideal Inclusions
• Corvantic logo
• Text "Membership Now Open"
• Web address: corvantic.com.au
Should not have
- Don't Use:
• Too much of the highlight colour
• Cartoon imagery
• Images that are too staged or revealing (clothing). Image should fit our target market of everyday active people, not elite athletes or models.

```html
<!DOCTYPE html>
<html lang="en">
<head>
<meta charset="utf-8">
<title>Corvantic Fitness Guild – Membership Poster</title>
<link rel="stylesheet" href="https://fonts.googleapis.com/css2?family=Oswald:wght@300;500;600&display=swap">
<style>
  :root {
    --stage: #2b2d30;
    --poster-black: #121212;
    --ink-white: #f2f2f2;
    --lime: #cefa08;
    --ink-dark: #141414;
  }
  * { box-sizing: border-box; margin: 0; padding: 0; }
  html, body {
    width: 1200px;
    height: 960px;
    overflow: hidden;
    background: var(--stage);
  }
  .poster {
    position: absolute;
    left: 300px;
    top: 30px;
    width: 600px;
    height: 900px;
    background: var(--poster-black);
    overflow: hidden;
    font-family: "Oswald", "Arial Narrow", sans-serif;
    color: var(--ink-white);
  }
  .hero-image {
    position: absolute;
    left: 220px;
    top: 250px;
    width: 380px;
    height: 650px;
    background:
      radial-gradient(ellipse 45% 40% at 62% 48%, rgba(224,101,30,0.85), rgba(110,36,16,0.55) 55%, rgba(18,18,18,0) 100%),
      radial-gradient(ellipse 55% 30% at 40% 70%, rgba(200,80,20,0.45), rgba(18,18,18,0) 100%);
  }
  .club-mark {
    position: absolute;
    left: 62px;
    top: 38px;
    font-weight: 600;
    font-size: 60px;
    line-height: 1;
    letter-spacing: 1px;
    white-space: nowrap;
  }
  .tagline {
    position: absolute;
    left: 62px;
    top: 150px;
    font-weight: 600;
    font-size: 58px;
    line-height: 64px;
    text-transform: uppercase;
    white-space: nowrap;
  }
  .cta {
    position: absolute;
    left: 62px;
    top: 440px;
    width: 190px;
    height: 68px;
    background: var(--lime);
    border-radius: 4px;
    color: var(--ink-dark);
    font-weight: 600;
    font-size: 44px;
    line-height: 68px;
    text-align: center;
    text-transform: uppercase;
    white-space: nowrap;
  }
  .intro {
    position: absolute;
    left: 62px;
    top: 600px;
    width: 320px;
    font-weight: 300;
    font-size: 14px;
    line-height: 21px;
  }
  .offer {
    position: absolute;
    left: 62px;
    top: 738px;
    width: 345px;
    padding: 3px 0 1px;
    border-top: 2px solid var(--lime);
    border-bottom: 2px solid var(--lime);
    font-weight: 600;
    font-size: 34px;
    line-height: 44px;
    text-transform: uppercase;
    white-space: nowrap;
  }
  .offer .highlight { color: var(--lime); }
  .brand-name {
    position: absolute;
    left: 62px;
    top: 832px;
    font-weight: 500;
    font-size: 32px;
    line-height: 40px;
    white-space: nowrap;
  }
  .web-address {
    position: absolute;
    right: 40px;
    top: 834px;
    font-weight: 600;
    font-size: 28px;
    line-height: 36px;
    white-space: nowrap;
  }
  .web-address .highlight { color: var(--lime); }
</style>
</head>
<body>
  <main class="poster">
    <div class="hero-image" role="img" aria-label="Photo of an athlete leaping with a basketball, wrapped in orange light trails"></div>

    <div class="club-mark">CFG</div>

    <h1 class="tagline">Shaping Steady,<br>Nimble,<br>Unbreakable<br>People</h1>

    <div class="cta">Join us</div>

    <p class="intro">A first of it's kind membership, The Corvantic Fitness Guild combines the skills of our industry-leading Physiotherapists, Strength Coaches and Massage Therapists into one membership with a tailored plan to guide you through the fundamentals of Movement, Mobility and Recovery.</p>

    <div class="offer">Membership <span class="highlight">Now Open</span></div>

    <div class="brand-name">Corvantic</div>
    <div class="web-address">www.<span class="highlight">corvantic</span>.com.au</div>
  </main>
</body>
</html>
```